Billboard - Cool Garden and Landscape Company (Brand Pack Included)

NEED A PROFESSIONAL BILLBOARD TO ADVERTISE OUR BUSINESS. HAVE MOCKED UP A SAMPLE CONCEPT BUT IT REQUIRES THE ICONS TO BE DEVELOPED TO A PROFESSIONAL STANDARD (I JUST COPIED RANDOM EXAMPLES FROM THE NET)

THE ICONS REPRESENT OUR KEY PRODUCT GROUPS. (These can be redesigned)
BILLBOARD IS 6M X 3M (SEE SPEC FILE ATTACHED) - IMAGE OF THE LOCATION ADDED TO THE FILES.

BRAND GUIDE INCLUDED WITH LOGO FILES

VISIT: https://www.facebook.com/Team.Fern.Crate/
Web: www.ferncrate.co.nz

Target Market(s)

Commuter traffic - busy road - Billboard site is on the left side approx 400m before our street turn off. Age group 30+ Home owners / Builders

Industry/Entity Type

Garden Supply

Font styles to use
Other font styles liked:
• comfortaa

Requirements
Must have
• No change to our logo or brand
• Next left
• Icons for products as per mock up - note these can be redesigned
Nice to have
• Easy to see at a distance
• Clean
• Simple

```html
<!DOCTYPE html>
<html lang="en">
<head>
<meta charset="utf-8">
<title>Fern Crate – Garden &amp; Landscape Supplies Billboard</title>
<link rel="stylesheet" href="https://fonts.googleapis.com/css2?family=Open+Sans:wght@700;800&display=swap">
<style>
  :root {
    --brand-green: #2da44a;
    --brand-orange: #f7941d;
    --ink-dark: #2a2a2a;
    --ink-grey: #8a8a8a;
    --paper: #ffffff;
    --backdrop: #eef1f3;
  }
  * { margin: 0; padding: 0; box-sizing: border-box; }
  html, body {
    width: 1200px; height: 900px; overflow: hidden;
    background: var(--backdrop);
  }
  .billboard {
    position: absolute; left: 50px; top: 175px;
    width: 1100px; height: 550px;
    background: var(--paper);
    overflow: hidden;
    box-shadow: 0 6px 24px rgba(0,0,0,0.12);
    font-family: "Open Sans", sans-serif;
  }
  .brand {
    position: absolute; left: 0; right: 0; top: 40px;
    display: flex; justify-content: center; align-items: center; gap: 14px;
  }
  .brand-square {
    width: 46px; height: 46px; background: var(--brand-green);
  }
  .brand-name {
    font-weight: 800; font-size: 50px; line-height: 1;
    letter-spacing: 1px; text-transform: uppercase;
    color: var(--brand-green);
  }
  .tagline {
    position: absolute; left: 0; right: 0; top: 106px;
    text-align: center;
    font-weight: 700; font-size: 20px; letter-spacing: 1px;
    color: var(--brand-orange);
  }
  .web-address {
    position: absolute; right: 40px; top: 52px;
    font-size: 20px; font-weight: 700; color: var(--ink-grey);
  }
  .headline {
    position: absolute; left: 0; right: 0; top: 160px;
    text-align: center;
    font-weight: 800; font-size: 46px; letter-spacing: 1px;
    text-transform: uppercase;
  }
  .headline .word-garden { color: var(--brand-green); }
  .headline .amp { color: var(--ink-grey); }
  .headline .word-landscape { color: var(--brand-orange); }
  .green-band {
    position: absolute; left: 0; right: 0; top: 268px; bottom: 0;
    background: var(--brand-green);
  }
  .product {
    position: absolute; top: 236px; width: 240px;
    text-align: center; color: var(--paper);
  }
  .product-badge { display: block; margin: 0 auto 10px; }
  .product-label {
    font-weight: 700; font-size: 22px; line-height: 1.3;
  }
  .product--firewood { left: 70px; }
  .product--compost { left: 265px; }
  .product--stone { left: 490px; }
  .product--trailers { left: 720px; }
  .address-bar {
    position: absolute; left: 0; top: 0; width: 1100px; height: 550px;
  }
  .address-text {
    position: absolute; left: 440px; right: 30px; top: 446px;
    text-align: center;
    font-weight: 800; font-size: 38px; color: var(--paper);
  }
  .next-left-label {
    position: absolute; left: 112px; top: 455px; width: 300px;
    text-align: center;
    font-weight: 800; font-size: 36px; color: var(--paper);
    text-transform: uppercase;
  }
</style>
</head>
<body>
  <main class="billboard">
    <div class="brand">
      <span class="brand-square"></span>
      <span class="brand-name">Fern Crate</span>
    </div>
    <div class="tagline">Grow Something Good</div>

    <div class="web-address">www.ferncrate.co.nz</div>

    <h1 class="headline">
      <span class="word-garden">Garden</span>
      <span class="amp">&amp;</span>
      <span class="word-landscape">Landscape Supplies</span>
    </h1>

    <div class="green-band"></div>

    <div class="product product--firewood">
      <svg class="product-badge" width="100" height="110" viewBox="0 0 100 110" role="img" aria-label="Firewood icon in orange hexagon">
        <polygon points="50,3 96,29 96,81 50,107 4,81 4,29" fill="var(--brand-orange)" stroke="#fff" stroke-width="4"/>
      </svg>
      <div class="product-label">Firewood<br>Fire Pellets</div>
    </div>

    <div class="product product--compost">
      <svg class="product-badge" width="100" height="110" viewBox="0 0 100 110" role="img" aria-label="Seedling in soil icon in orange hexagon">
        <polygon points="50,3 96,29 96,81 50,107 4,81 4,29" fill="var(--brand-orange)" stroke="#fff" stroke-width="4"/>
      </svg>
      <div class="product-label">Compost<br>Soil + Mulch</div>
    </div>

    <div class="product product--stone">
      <svg class="product-badge" width="100" height="110" viewBox="0 0 100 110" role="img" aria-label="Stacked stones icon in orange hexagon">
        <polygon points="50,3 96,29 96,81 50,107 4,81 4,29" fill="var(--brand-orange)" stroke="#fff" stroke-width="4"/>
      </svg>
      <div class="product-label">Decorative Stone<br>Aggregates</div>
    </div>

    <div class="product product--trailers">
      <svg class="product-badge" width="100" height="110" viewBox="0 0 100 110" role="img" aria-label="Trailer icon in orange hexagon">
        <polygon points="50,3 96,29 96,81 50,107 4,81 4,29" fill="var(--brand-orange)" stroke="#fff" stroke-width="4"/>
      </svg>
      <div class="product-label">Hire Trailers<br>Delivery</div>
    </div>

    <svg class="address-bar" viewBox="0 0 1100 550" aria-hidden="true">
      <polygon points="445,432 1100,432 1100,512 415,512" fill="var(--ink-dark)"/>
      <polygon points="425,426 425,518 120,518 120,540 28,472 120,404 120,426"
               fill="var(--brand-orange)" stroke="#fff" stroke-width="4" stroke-linejoin="miter"/>
    </svg>
    <div class="next-left-label">Next Left</div>
    <div class="address-text">48 Harlow Road (off Bramleigh)</div>
  </main>
</body>
</html>
```